Website Design for Marlowe Institute

Marlowe Institute is a new start up professional college established to meet the educational needs of young adults, working adults, organisations and employers. We offer a variety of programs ranging from ICT, Healthcare, Business, Aviation, Professional courses. We will also be providing online courses in the very near future
We would like a modern, fresh conservative, sophisticated and professional appealing website for students. We want to keep our logo the same with the logo colours blended in as the primary colours and focus.
Unless you have a good reason for not, we would like the page to be the whole with of the screen like many websites are for the moment. The colour scheme should have a white or very light background.
We need a sliding header with pictures of young adults and professional people in college, pictures of Harare City, Students in a computer lab, adults students in Healthcare uniforms, etc…. Please see http://www.brightmeadcampus.com/
Main menu items: Home, About Us, Programs (When you hover the mouse on Programs, we should see the different Schools in the Academy. Business School, Healthcare School, ICT School, Hair & Beauty School, Aviation School, Executive School), Admissions (downloadable application form in PDF), International Students, News & Events, Contact Us
We need 10 pages designed as a start. These need to be scalable as we will be adding more pages when we start adding the content: The home page can be considerably different from the other pages. It needs to grab the attention of students and parents and direct them where they need to go e.g. the Academy schools. These should be visible on the home page as in the http://www.brightmeadcampus.com/ when clicked the School should open in a different page. That page will also have sub-pages for the individual courses within the School
The home page should include a scrolling widget where we can put our affiliated organisations. This should be at the bottom but before the Site map
An element of lead generation (either form fields or link to contact form should be included (for instance, “apply now” or “request more information” type buttons ).
Inspirational website & template:
http://www.brightmeadcampus.com/
http://www.pelvorth.com/Zenta-College-Layout-template-482930615.html
Our website objective is to
Provides information to prospective students about the Academy programs, we offer etc
1. Impress our participants with our fresh vibrant website design
2. User friendly with necessary info all seen on home page without scrolling down yet.
3. create awareness
4.will be integrating with facebook and twitter
The website should be:
- Easy to navigate
- SEO friendly design
Home page
Target Market(s)
Our Target market is the ages of 18-40yrs Professionals and non professionals
On High Income
Industry/Entity Type
Education
Number of Pages Required
5+ page
Requirements
Must have
- Must be responsive
- Data which I will provide later
Nice to have
- Would be great if you can get the same template as this one http://www.brightmeadcampus.com/ or a much better one
Should not have
- No too much page scrolling
- Not too squashed
- Avoid Too many colours

```html
<!DOCTYPE html>
<html lang="en">
<head>
<meta charset="utf-8">
<title>Marlowe Institute — Home</title>
<link href="https://fonts.googleapis.com/css2?family=Open+Sans:wght@400;600;700;800&display=swap" rel="stylesheet">
<style>
:root{
  --navy:#1b2d4b;
  --navy-dark:#132238;
  --navy-deep:#0e1a2c;
  --gold:#f2b01e;
  --gold-dark:#d99a0f;
  --page:#e8eaed;
  --panel:#ffffff;
  --band:#f1f2f4;
  --text:#333a45;
  --muted:#7c8491;
  --line:#d9dde3;
}
*{box-sizing:border-box;margin:0;padding:0}
html,body{width:1200px;height:2604px;overflow:hidden}
body{background:var(--page);font-family:"Open Sans",Arial,sans-serif;color:var(--text);font-size:12px}
.container{width:940px;margin:0 auto;position:relative}
.btn{display:inline-block;background:var(--navy);color:#fff;font-weight:700;font-size:10px;letter-spacing:.5px;padding:7px 14px;text-transform:uppercase}
.btn-gold{background:var(--gold);color:var(--navy)}
.section-title{font-size:20px;font-weight:600;color:var(--navy)}

/* header */
.topbar{height:80px;background:#fff}
.topbar .container{height:80px;display:flex;align-items:center;justify-content:space-between}
.brand{display:flex;align-items:center;gap:10px}
.brand-mark{width:30px;height:30px;background:var(--navy)}
.brand-name{font-size:22px;font-weight:700;color:var(--navy)}
.phone{font-size:14px;color:var(--muted);display:flex;align-items:center;gap:6px}
.phone b{color:var(--gold);font-weight:700}

.mainnav{height:32px}
.mainnav .container{height:32px;background:var(--navy);display:flex;align-items:center}
.mainnav a{color:#fff;font-size:10px;font-weight:600;padding:0 14px;height:32px;line-height:32px;text-transform:uppercase}
.mainnav a.active{background:var(--gold);color:var(--navy)}
.search{margin-left:auto;margin-right:8px;width:150px;height:20px;background:#fff;display:flex;align-items:center;justify-content:space-between;padding:0 6px;color:var(--muted);font-size:9px}

.hero{height:416px}
.hero .container{height:416px;background:linear-gradient(120deg,#c8b9a4 0%,#8b7a6a 35%,#d9cfc4 65%,#f3efe9 100%)}
.hero-copy{position:absolute;left:40px;top:166px;font-weight:800;font-size:42px;line-height:46px;color:#fff;text-transform:uppercase}
.hero-copy span{color:var(--gold)}

/* courses */
.courses{height:380px;margin-top:32px}
.courses .container{height:380px;background:var(--panel);display:flex;padding:36px 30px}
.finder{width:200px;border:1px solid var(--line);align-self:flex-start}
.finder h3{background:var(--navy);color:#fff;font-size:14px;font-weight:600;padding:10px 12px}
.finder li{list-style:none;font-size:10px;padding:0 12px;height:34px;line-height:34px;border-top:1px solid var(--line);display:flex;align-items:center;gap:8px;color:var(--navy)}
.finder li:before{content:"";width:5px;height:5px;background:var(--navy)}
.finder li.active{background:var(--gold);font-weight:600}
.schools{flex:1;margin-left:30px}
.schools h2{font-size:16px;font-weight:700;color:var(--navy);margin:6px 0 12px}
.school-grid{display:flex;gap:18px}
.school{flex:1;border:1px solid var(--line);height:228px;display:flex;flex-direction:column}
.school-photo{height:110px;position:relative}
.school-label{position:absolute;left:0;right:0;bottom:0;background:var(--navy);color:#fff;font-size:10px;font-weight:700;text-align:center;padding:6px 0}
.school-body{flex:1;padding:10px 12px;font-size:9px;line-height:13px;color:var(--muted);text-align:center}
.school-body .btn{margin-top:10px}
.school.featured .school-body{background:var(--gold);color:var(--navy)}
.school.featured .school-label{background:var(--gold);color:var(--navy)}

/* about */
.about{height:150px;margin-top:20px;background:var(--band)}
.about .container{height:150px;padding:28px 30px}
.about p{width:720px;margin-top:10px;font-size:10px;line-height:15px;color:var(--muted)}
.about .btn{position:absolute;right:30px;top:76px}

/* news row */
.news-row{height:300px;margin-top:30px}
.news-row .container{height:300px;background:var(--panel);display:flex;gap:40px;padding:24px 30px}
.col{flex:1}
.col h3{font-size:16px;font-weight:600;color:var(--navy);padding-bottom:8px;border-bottom:1px solid var(--line);margin-bottom:14px}
.news-item{display:flex;gap:12px;margin-bottom:14px}
.news-thumb{width:44px;height:44px;flex:none}
.news-item p{font-size:9px;line-height:13px;color:var(--text)}
.news-item time{display:block;font-size:8px;color:var(--muted);margin-top:3px}
.video{height:170px;background:linear-gradient(135deg,#2a3340,#6b5560 50%,#a44 100%);position:relative}
.video svg{position:absolute;left:50%;top:50%;margin:-20px 0 0 -20px}
.form .field{height:24px;border:1px solid var(--line);margin-bottom:8px;font-size:9px;color:var(--muted);line-height:22px;padding:0 8px}
.form .btn{float:right}

/* testimonials */
.testimonials{height:260px;margin-top:20px;background:var(--navy)}
.testimonials .container{height:260px;padding:36px 30px;color:#fff}
.testimonials h2{font-size:20px;font-weight:600}
.arrows{position:absolute;right:30px;top:40px;display:flex;gap:10px}
.quote{display:flex;gap:30px;margin-top:36px;align-items:flex-start}
.avatar{width:96px;height:96px;border-radius:50%;background:radial-gradient(circle,#c9a689,#6d5948);flex:none;border:3px solid #fff}
.quote p{font-size:11px;line-height:18px;color:#d7dde7;font-style:italic;width:640px}
.quote .who{margin-top:10px;font-size:10px;color:#c5cbd5;font-style:normal}
.quote .who b{color:var(--gold);font-weight:700;margin-right:6px}
.quote-mark{font-size:40px;line-height:30px;color:var(--gold);font-weight:800}

/* promos */
.promos{height:320px;margin-top:40px}
.promos .container{height:320px;display:flex;gap:30px}
.promo{flex:1;background:var(--panel);padding:14px}
.promo-media{height:180px;position:relative}
.promo-bar{position:absolute;left:0;right:0;bottom:0;background:var(--navy);color:#fff;text-align:center;font-size:11px;font-weight:700;padding:7px 0;text-transform:uppercase}
.promo h3{font-size:15px;font-weight:600;color:var(--navy);margin-top:14px;text-align:center}
.promo p{font-size:9px;color:var(--muted);line-height:13px;margin-top:4px;text-align:center}
.promo .btn{margin-top:10px}
.promo .center{text-align:center}

/* partners */
.partners{height:130px;margin-top:20px}
.partners .container{height:130px;background:var(--panel);display:flex;align-items:center;justify-content:space-around;padding:0 30px}
.partner{display:flex;align-items:center;gap:8px;font-size:18px;font-weight:600;color:#5b6270}
.partner i{width:22px;height:22px;background:#9aa1ab;display:block}
.partner i.round{border-radius:50%}

/* footer */
.site-footer{height:300px;margin-top:30px;background:var(--navy)}
.site-footer .container{height:300px;display:flex;gap:40px;padding:44px 30px 0}
.fcol{width:170px}
.fcol.wide{width:260px;margin-left:auto}
.fcol h4{font-size:11px;font-weight:700;color:#fff;letter-spacing:1px;margin-bottom:12px;text-transform:uppercase}
.fcol li{list-style:none;font-size:9px;color:#a9b3c3;line-height:17px}
.subscribe{display:flex;height:28px;margin-bottom:10px}
.subscribe span{flex:1;background:var(--navy-dark);border:1px solid #3a4d6c;color:#8f9bb0;font-size:9px;line-height:26px;padding:0 8px}
.subscribe b{width:30px;background:var(--navy-dark);border:1px solid #3a4d6c;border-left:none;display:flex;align-items:center;justify-content:center}
.socials{display:flex;gap:8px;justify-content:flex-end;margin-top:40px}
.socials i{width:14px;height:14px;border-radius:50%;background:#6f7f99;display:block}
.bottom{height:44px;background:var(--navy-deep)}
.bottom .container{height:44px;display:flex;align-items:center;justify-content:space-between;padding:0 30px}
.bottom .brand-name{font-size:13px;color:#fff}
.bottom .brand-mark{width:16px;height:16px;background:#fff}
.bottom small{font-size:8px;color:#7c889c}
</style>
</head>
<body>

<header class="topbar">
  <div class="container">
    <div class="brand"><span class="brand-mark"></span><span class="brand-name">Marlowe Institute</span></div>
    <div class="phone">
      <svg width="12" height="12" viewBox="0 0 24 24"><path fill="#f2b01e" d="M6.6 10.8a15 15 0 0 0 6.6 6.6l2.2-2.2c.3-.3.7-.4 1-.2 1.1.4 2.3.6 3.6.6.6 0 1 .4 1 1V20c0 .6-.4 1-1 1A17 17 0 0 1 3 4c0-.6.4-1 1-1h3.5c.6 0 1 .4 1 1 0 1.3.2 2.5.6 3.6.1.3 0 .7-.2 1z"/></svg>
      CALL US: <b>+44 (0) 20 7946 0321</b>
    </div>
  </div>
</header>

<nav class="mainnav">
  <div class="container">
    <a class="active">Home</a><a>About Us</a><a>Programs</a><a>International Students</a><a>News &amp; Events</a><a>Contact Us</a>
    <div class="search">Search here...
      <svg width="10" height="10" viewBox="0 0 24 24"><circle cx="10" cy="10" r="7" fill="none" stroke="#7c8491" stroke-width="3"/><path d="M15 15l6 6" stroke="#7c8491" stroke-width="3"/></svg>
    </div>
  </div>
</nav>

<section class="hero">
  <div class="container" role="img" aria-label="Photo of smiling young adult students studying together at laptops in a classroom">
    <h1 class="hero-copy">Welcome to<br><span>Marlowe Institute</span></h1>
  </div>
</section>

<section class="courses">
  <div class="container">
    <aside class="finder">
      <h3>Find a Course</h3>
      <ul>
        <li class="active">Hair &amp; Beauty School</li>
        <li>Healthcare School</li>
        <li>Business School</li>
        <li>Executive School</li>
        <li>Aviation School</li>
        <li>ICT School</li>
      </ul>
    </aside>
    <div class="schools">
      <h2>HAIR &amp; BEAUTY SCHOOL</h2>
      <div class="school-grid">
        <article class="school featured">
          <div class="school-photo" role="img" aria-label="Photo of a stylist working in a beauty salon" style="background:linear-gradient(135deg,#d8c2ae,#8a6d58)"><div class="school-label">HAIR &amp; BEAUTY SCHOOL</div></div>
          <div class="school-body">Practical salon training with industry tutors and modern equipment for every learner.<br><span class="btn">Read More</span></div>
        </article>
        <article class="school">
          <div class="school-photo" role="img" aria-label="Photo of healthcare students in uniform" style="background:linear-gradient(135deg,#b9c9d8,#5b6f86)"><div class="school-label">HEALTHCARE SCHOOL</div></div>
          <div class="school-body">Care and nursing programmes with clinical placements and hands-on practice sessions.<br><span class="btn btn-gold">Read More</span></div>
        </article>
        <article class="school">
          <div class="school-photo" role="img" aria-label="Photo of business students in a meeting" style="background:linear-gradient(135deg,#c3b8a8,#6c6157)"><div class="school-label">BUSINESS SCHOOL</div></div>
          <div class="school-body">Management, finance and marketing courses built around real workplace projects.<br><span class="btn btn-gold">Read More</span></div>
        </article>
      </div>
    </div>
  </div>
</section>

<section class="about">
  <div class="container">
    <h2 class="section-title">About Us</h2>
    <p>Marlowe Institute is a new professional college serving young adults, working adults and employers. We offer programmes in ICT, healthcare, business, aviation and professional studies, taught by experienced tutors in modern facilities. Our courses combine classroom learning with practical experience so students leave ready for work, and online courses will follow very soon for learners who study from home.</p>
    <span class="btn">Learn More</span>
  </div>
</section>

<section class="news-row">
  <div class="container">
    <div class="col">
      <h3>Recent News</h3>
      <div class="news-item"><div class="news-thumb" role="img" aria-label="Photo of a student" style="background:#b69a84"></div><p>New evening classes open for adult learners this term.<time>17 May 2015</time></p></div>
      <div class="news-item"><div class="news-thumb" role="img" aria-label="Photo of a student" style="background:#8d9db0"></div><p>Healthcare students complete their first hospital placement.<time>22 May 2015</time></p></div>
      <div class="news-item"><div class="news-thumb" role="img" aria-label="Photo of a student" style="background:#9fa88a"></div><p>Open day welcomes families to the new campus building.<time>29 May 2015</time></p></div>
    </div>
    <div class="col">
      <h3>Workshop</h3>
      <div class="video" role="img" aria-label="Video still of a workshop session">
        <svg width="40" height="40" viewBox="0 0 40 40"><circle cx="20" cy="20" r="19" fill="#fff" opacity=".9"/><path d="M16 12l12 8-12 8z" fill="#c0392b"/></svg>
      </div>
    </div>
    <div class="col form">
      <h3>Online Application</h3>
      <div class="field">Full Name</div>
      <div class="field">Email Address</div>
      <div class="field">Phone Number</div>
      <div class="field">Course of Interest</div>
      <span class="btn">Apply Now</span>
    </div>
  </div>
</section>

<section class="testimonials">
  <div class="container">
    <h2>Student Testimonials</h2>
    <div class="arrows">
      <svg width="12" height="12" viewBox="0 0 12 12"><path d="M8 1L3 6l5 5" fill="none" stroke="#fff" stroke-width="2"/></svg>
      <svg width="12" height="12" viewBox="0 0 12 12"><path d="M4 1l5 5-5 5" fill="none" stroke="#fff" stroke-width="2"/></svg>
    </div>
    <div class="quote">
      <div class="avatar" role="img" aria-label="Portrait photo of a student"></div>
      <div class="quote-mark">&ldquo;</div>
      <div>
        <p>The tutors here really care about how we progress. I joined the evening business course while working full time, and the flexible timetable made it possible. The practical projects gave me confidence, and within months I was promoted at work. I would recommend it to anyone.</p>
        <div class="who"><b>Learn More</b>Student</div>
      </div>
    </div>
  </div>
</section>

<section class="promos">
  <div class="container">
    <div class="promo">
      <div class="promo-media" role="img" aria-label="Photo of students studying in a computer lab" style="background:linear-gradient(135deg,#cfb89d,#7d6a58)"><div class="promo-bar">Coming Soon: New Courses</div></div>
      <h3>New Courses</h3>
      <p>Online study options are on the way for next year.</p>
    </div>
    <div class="promo">
      <div class="promo-media" role="img" aria-label="Street map showing the campus location" style="background:linear-gradient(135deg,#e4e7ee,#c3cad8)"></div>
      <h3>Visit Us</h3>
      <p>Find our campus and plan your visit to meet our staff.</p>
      <div class="center"><span class="btn">Click Here for Location Map</span></div>
    </div>
    <div class="promo">
      <div class="promo-media" role="img" aria-label="Printed course guide brochures" style="background:linear-gradient(135deg,#dfe3ea,#4f6a93)"></div>
      <h3>Download a Course Guide</h3>
      <p>Everything you need to know about our programmes.</p>
      <div class="center"><span class="btn">Download</span></div>
    </div>
  </div>
</section>

<section class="partners">
  <div class="container">
    <div class="partner"><i class="round"></i>Harbourline</div>
    <div class="partner"><i></i>Tidewell Resorts</div>
    <div class="partner"><i class="round"></i>Crestmoor Group</div>
    <div class="partner"><i></i>Northvale Partners</div>
  </div>
</section>

<footer class="site-footer">
  <div class="container">
    <div class="fcol"><h4>Company</h4><ul><li>About Us</li><li>Our Team</li><li>Careers</li><li>Contact Us</li></ul></div>
    <div class="fcol"><h4>Work</h4><ul><li>International Students</li><li>Admissions</li><li>Programs</li></ul></div>
    <div class="fcol"><h4>Services</h4><ul><li>ICT</li><li>Healthcare</li><li>Business</li><li>Aviation</li><li>Professional Courses</li></ul></div>
    <div class="fcol wide"><h4>Keep up with Marlowe</h4>
      <div class="subscribe"><span>Enter email address</span><b><svg width="10" height="10" viewBox="0 0 10 10"><path d="M1 5h7M5 2l3 3-3 3" fill="none" stroke="#fff" stroke-width="1.5"/></svg></b></div>
      <ul><li>Subscribe to news</li></ul>
      <div class="socials"><i></i><i></i><i></i></div>
    </div>
  </div>
</footer>
<div class="bottom">
  <div class="container">
    <div class="brand"><span class="brand-mark"></span><span class="brand-name">Marlowe Institute</span></div>
    <small>© 2015 Marlowe Institute. All rights reserved.</small>
  </div>
</div>

</body>
</html>
```